Corvantis websites redesign

Www.cor-vantis.com needs to be redesigned along with updations. The incremental material will be provided for the updations. We are looking for complete redesign of the pages with the new content. The complete write up will be provided soon

Target Market(s)

Global

Coding

Coded - Design and coding required

Number of Pages Required

5+ page

Requirements
Must have
• A clean and slick design for the Consulting.
Should not have
• Too many pictures which reduces the speed of the site

```html
<!DOCTYPE html>
<html lang="en">
<head>
<meta charset="utf-8">
<title>Corvantis</title>
<link href="https://fonts.googleapis.com/css2?family=Catamaran:wght@400;500&family=Prata&display=swap" rel="stylesheet">
<style>
  :root {
    --maroon: #5e2022;
    --blue: #35a9e0;
    --blue-nav: #38a6d4;
    --white: #ffffff;
    --ink: #3b3b3b;
    --logo-ink: #3a3f5c;
  }
  html, body { margin: 0; padding: 0; overflow: hidden; }
  .page {
    position: relative;
    width: 975px;
    height: 1200px;
    overflow: hidden;
    font-family: "Prata", serif;
    color: var(--white);
  }
  .backdrop {
    position: absolute; inset: 0;
    background:
      radial-gradient(ellipse at 70% 30%, #d9d4cb 0%, rgba(217,212,203,0) 55%),
      radial-gradient(ellipse at 20% 85%, #e6e9ec 0%, rgba(230,233,236,0) 45%),
      linear-gradient(180deg, #c9c2b8 0%, #a89c8c 35%, #6b5a4d 60%, #3e342f 85%, #5a524d 100%);
  }
  .disc { position: absolute; border-radius: 50%; }
  .masthead-ring { left: 240px; top: -292px; width: 492px; height: 492px; background: var(--maroon); }
  .masthead-face { left: 270px; top: -252px; width: 432px; height: 432px; background: var(--white); }
  .brand {
    position: absolute; left: 385px; top: 56px;
    display: flex; align-items: center; gap: 10px;
    font-family: "Catamaran", sans-serif; font-weight: 500; font-size: 30px;
    color: var(--logo-ink);
  }
  .brand-dot { width: 34px; height: 34px; border-radius: 50%; background: var(--maroon); }

  .footer-ring { left: 240px; top: 994px; width: 492px; height: 492px; background: var(--maroon); }
  .footer-face { left: 270px; top: 1028px; width: 432px; height: 432px; background: var(--white); }
  .footer-mail {
    position: absolute; left: 0; width: 975px; top: 1055px; text-align: center;
    font-family: "Catamaran", sans-serif; color: var(--ink);
  }
  .footer-mail svg { display: block; margin: 0 auto 2px; }
  .footer-mail .address { font-size: 15px; letter-spacing: .3px; }
  .footer-rule { position: absolute; left: 312px; top: 1134px; width: 352px; height: 1px; background: #6a6a6a; }
  .copyright {
    position: absolute; left: 0; width: 975px; top: 1150px; text-align: center;
    font-family: "Catamaran", sans-serif; font-size: 9px; color: #333;
  }

  .side-ring { width: 500px; height: 500px; background: var(--white); top: 334px; box-shadow: 0 0 14px rgba(0,0,0,.25); }
  .side-face { width: 456px; height: 456px; background: var(--maroon); top: 356px; }
  .social-ring { left: -294px; }
  .social-face { left: -274px; }
  .contact-ring { left: 772px; }
  .contact-face { left: 796px; }

  .social-list { position: absolute; left: 0; top: 0; }
  .social-row { position: absolute; left: 0; width: 168px; height: 1px; background: rgba(255,255,255,.35); }
  .social-row span {
    position: absolute; left: 43px; top: -20px; width: 38px; height: 38px;
    border: 1px solid rgba(255,255,255,.55); border-radius: 50%;
  }
  .phone-row { position: absolute; left: 800px; width: 175px; height: 1px; background: rgba(255,255,255,.35); }
  .phone-row .badge {
    position: absolute; left: 74px; top: -16px; width: 30px; height: 30px;
    border: 1px solid rgba(255,255,255,.6); border-radius: 50%; background: var(--maroon);
    display: flex; align-items: center; justify-content: center;
  }
  .phone-number { position: absolute; left: 800px; width: 190px; text-align: center; font-size: 17px; }

  .nav-bubble {
    position: absolute; width: 180px; height: 180px; border-radius: 50%;
    background: var(--blue-nav); border: 13px solid var(--white);
    box-shadow: 0 0 16px rgba(0,0,0,.3);
    display: flex; flex-direction: column; align-items: center; justify-content: center;
    font-size: 20px; letter-spacing: .3px;
  }
  .nav-bubble svg { margin-bottom: 8px; }
  .nav-home { left: 43px; top: 83px; }
  .nav-about { left: 729px; top: 83px; }
  .nav-testimonials { left: 43px; top: 891px; font-size: 18px; }
  .nav-contact { left: 729px; top: 891px; }

  .tile {
    position: absolute; width: 218px; height: 218px;
    background: var(--blue); border: 11px solid var(--white);
    box-shadow: 0 0 14px rgba(0,0,0,.3);
    display: flex; flex-direction: column; align-items: center; justify-content: center;
    font-size: 20px; letter-spacing: .3px;
  }
  .tile svg { margin-bottom: 12px; }
  .tile-founder { left: 244px; top: 348px; border-radius: 8px 50% 50% 50%; transform: rotate(1deg); }
  .tile-consultancy { left: 508px; top: 348px; border-radius: 50% 8px 50% 50%; transform: rotate(-1deg); }
  .tile-system { left: 244px; top: 652px; border-radius: 50% 50% 50% 8px; transform: rotate(-1deg); }
  .tile-cases { left: 508px; top: 652px; border-radius: 50% 50% 8px 50%; transform: rotate(1deg); }
</style>
</head>
<body>
<div class="page">
  <div class="backdrop" role="img" aria-label="Blurred photo of a business person working at a desk with a laptop, pen and papers"></div>

  <div class="disc masthead-ring"></div>
  <div class="disc masthead-face"></div>
  <div class="brand"><span class="brand-dot"></span>Corvantis</div>

  <div class="disc side-ring social-ring"></div>
  <div class="disc side-face social-face"></div>
  <div class="social-list" aria-label="Social links">
    <div class="social-row" style="top:508px"><span></span></div>
    <div class="social-row" style="top:564px"><span></span></div>
    <div class="social-row" style="top:622px"><span></span></div>
    <div class="social-row" style="top:681px"><span></span></div>
  </div>

  <div class="disc side-ring contact-ring"></div>
  <div class="disc side-face contact-face"></div>
  <div class="phone-row" style="top:528px"><span class="badge">
    <svg width="14" height="14" viewBox="0 0 24 24"><path fill="#fff" d="M6.6 10.8a15.1 15.1 0 0 0 6.6 6.6l2.2-2.2c.3-.3.7-.4 1-.2 1.1.4 2.3.6 3.6.6.6 0 1 .4 1 1V20c0 .6-.4 1-1 1C10.6 21 3 13.4 3 4c0-.6.4-1 1-1h3.5c.6 0 1 .4 1 1 0 1.3.2 2.5.6 3.6.1.3 0 .7-.2 1z"/></svg>
  </span></div>
  <div class="phone-number" style="top:552px">123-456-7890</div>
  <div class="phone-row" style="top:606px"><span class="badge">
    <svg width="13" height="13" viewBox="0 0 24 24"><rect x="5" y="3" width="14" height="18" rx="2" fill="#fff"/><rect x="8" y="6" width="8" height="4" fill="#5e2022"/><rect x="8" y="12" width="2" height="2" fill="#5e2022"/><rect x="11" y="12" width="2" height="2" fill="#5e2022"/><rect x="14" y="12" width="2" height="2" fill="#5e2022"/><rect x="8" y="15" width="2" height="2" fill="#5e2022"/><rect x="11" y="15" width="2" height="2" fill="#5e2022"/><rect x="14" y="15" width="2" height="2" fill="#5e2022"/></svg>
  </span></div>
  <div class="phone-number" style="top:627px">123-456-7890</div>

  <div class="nav-bubble nav-home">
    <svg width="42" height="34" viewBox="0 0 42 34"><path fill="#fff" d="M21 2 2 18l3 3 3-2.5V33h10V24h6v9h10V18.5l3 2.5 3-3L33 10V3h-5v3z"/></svg>
    HOME
  </div>
  <div class="nav-bubble nav-about">
    <svg width="44" height="44" viewBox="0 0 44 44"><circle cx="22" cy="22" r="18" fill="none" stroke="#fff" stroke-width="7"/><circle cx="22" cy="22" r="8" fill="var(--blue-nav)" stroke="#fff" stroke-width="2"/></svg>
    ABOUT US
  </div>
  <div class="nav-bubble nav-testimonials">
    <svg width="38" height="28" viewBox="0 0 38 28"><rect x="2" y="2" width="34" height="24" rx="2" fill="none" stroke="#fff" stroke-width="3"/><path d="M3 4l16 12L35 4" fill="none" stroke="#fff" stroke-width="3"/></svg>
    TESTIMONILAS
  </div>
  <div class="nav-bubble nav-contact">
    <svg width="26" height="34" viewBox="0 0 26 34"><path fill="#fff" d="M13 1a12 12 0 0 0-12 12c0 9 12 20 12 20s12-11 12-20A12 12 0 0 0 13 1zm0 17a5 5 0 1 1 0-10 5 5 0 0 1 0 10z"/></svg>
    CONTACT US
  </div>

  <div class="tile tile-founder">
    <svg width="56" height="68" viewBox="0 0 56 68"><ellipse cx="28" cy="17" rx="12" ry="15" fill="#fff"/><path fill="#fff" d="M2 66c0-16 8-26 18-29l8 10 8-10c10 3 18 13 18 29z"/><path fill="var(--blue)" d="M26 40h4l1 4-3 14-3-14z"/></svg>
    FOUNDER
  </div>
  <div class="tile tile-consultancy">
    <svg width="90" height="50" viewBox="0 0 90 50"><rect x="2" y="4" width="12" height="44" fill="#fff"/><rect x="76" y="4" width="12" height="44" fill="#fff"/><path fill="#fff" d="M16 10h14l10-4 20 8h14v24h-8L50 46H40L16 32z"/><path d="M32 16l12 10 6-3" fill="none" stroke="var(--blue)" stroke-width="2"/></svg>
    CONSULTANCY
  </div>
  <div class="tile tile-system">
    <svg width="68" height="62" viewBox="0 0 68 62"><rect x="3" y="3" width="62" height="42" rx="3" fill="none" stroke="#fff" stroke-width="5"/><path d="M22 24l9 9 16-17" fill="none" stroke="#fff" stroke-width="6"/><rect x="28" y="46" width="12" height="8" fill="#fff"/><rect x="16" y="54" width="36" height="5" fill="#fff"/></svg>
    SYSTEM
  </div>
  <div class="tile tile-cases">
    <svg width="70" height="66" viewBox="0 0 70 66"><path d="M3 3h30l12 12v46H3z" fill="none" stroke="#fff" stroke-width="4"/><path fill="#fff" d="M9 16h16v3H9zm0 7h14v3H9zm0 7h12v3H9zm0 7h14v3H9zm0 7h20v3H9z"/><circle cx="42" cy="36" r="12" fill="var(--blue)" stroke="#fff" stroke-width="4"/><path d="M51 45l14 14" stroke="#fff" stroke-width="6"/><path fill="#fff" d="M37 31h10v3H37zm0 6h10v3H37z"/></svg>
    CASE STUDIES
  </div>

  <div class="disc footer-ring"></div>
  <div class="disc footer-face"></div>
  <div class="footer-mail">
    <svg width="30" height="22" viewBox="0 0 30 22"><rect x="0" y="0" width="30" height="22" rx="2" fill="var(--maroon)"/><path d="M1 2l14 11L29 2" fill="none" stroke="#fff" stroke-width="2"/></svg>
    <span class="address">info@companyname.com</span>
  </div>
  <div class="footer-rule"></div>
  <div class="copyright">Copyright 2016 Comapny Name. All Rights Reserved.</div>
</div>
</body>
</html>
```